Fenwick & Associates Holdings Business Cards

Max 4/4 (4 Colors each side) Business Cards
Size 85 x 55 mm
Fenwick & Associates Holdings Ltd. (3 Versions of the Logo attached)
Possibility to add second company name as we have different subsidiary companies
Name, Position, E-Mail, Direct Phone, (optional Cell Phone)
Possibility to change the address as we have offices in London an Zurich
Font for Name, Address, etc.: Source Sans Pro Light (Google Fonts)
PDF and Source Files to send them directly to offset

Industry/Entity Type

Business

Font styles to use
Sans Serif
Script

```html
<!DOCTYPE html>
<html lang="en">
<head>
<meta charset="utf-8">
<title>Fenwick &amp; Associates Holdings – Business Cards</title>
<link rel="stylesheet" href="https://fonts.googleapis.com/css2?family=Libre+Baskerville&family=Source+Sans+3:wght@300;400&display=swap">
<style>
  :root {
    --backdrop: #d9d9d9;
    --card-front: #f7f7f8;
    --card-back: #f4f8fc;
    --brand-blue: #1d4f8c;
    --ink: #222428;
    --rule: #c9ccd2;
    --pattern-a: #f2eef0;
    --pattern-b: #e9eef3;
  }
  * { margin: 0; padding: 0; box-sizing: border-box; }
  html, body { width: 900px; height: 1200px; overflow: hidden; }
  body { background: var(--backdrop); position: relative; font-family: "Source Sans 3", Arial, sans-serif; }

  .card { position: absolute; left: 15px; width: 870px; box-shadow: 0 1px 4px rgba(0,0,0,.18); overflow: hidden; }
  .card-front { top: 15px; height: 564px; background: var(--card-front); }
  .card-back { top: 615px; height: 570px; background: var(--card-back); }

  .front-texture {
    position: absolute; inset: 0;
    background: linear-gradient(135deg, var(--pattern-a) 0%, #fbfbfc 40%, var(--pattern-b) 75%, #f6f2f4 100%);
  }

  .brand-mark { position: absolute; background: var(--brand-blue); }
  .card-front .brand-mark { left: 370px; top: 162px; width: 130px; height: 130px; }
  .card-back .brand-mark { left: 407px; top: 78px; width: 56px; height: 56px; }

  .company-name {
    position: absolute; left: 0; right: 0; text-align: center;
    font-family: "Libre Baskerville", Georgia, serif;
    color: var(--brand-blue); font-weight: 400; white-space: nowrap; line-height: 1.2;
  }
  .card-front .company-name { top: 355px; font-size: 33px; letter-spacing: 1px; }
  .card-back .company-name { top: 174px; font-size: 18px; letter-spacing: .5px; }

  .contact { position: absolute; top: 276px; left: 0; width: 100%; height: 290px; font-size: 33px; font-weight: 400; color: var(--ink); line-height: 42px; }
  .contact .label { position: absolute; width: 30px; }
  .contact .value { position: absolute; white-space: nowrap; }
  .contact .rule { position: absolute; top: 4px; width: 1px; height: 284px; background: var(--rule); }
</style>
</head>
<body>
  <section class="card card-front">
    <div class="front-texture" role="img" aria-label="Soft faceted background texture in pale grey and blush tones"></div>
    <div class="brand-mark"></div>
    <div class="company-name">FENWICK &amp; ASSOCIATES HOLDINGS</div>
  </section>

  <section class="card card-back">
    <div class="brand-mark"></div>
    <div class="company-name">FENWICK &amp; ASSOCIATES HOLDINGS</div>
    <div class="contact">
      <span class="label" style="left:133px;top:0">T</span>
      <span class="label" style="left:133px;top:42px">E</span>
      <span class="rule" style="left:156px"></span>
      <span class="value" style="left:168px;top:0">00000000000</span>
      <span class="value" style="left:168px;top:42px">email@email.com</span>
      <span class="label" style="left:447px;top:0">A</span>
      <span class="rule" style="left:477px"></span>
      <span class="value" style="left:489px;top:0">00 address</span>
      <span class="value" style="left:489px;top:42px">address</span>
      <span class="value" style="left:489px;top:84px">address</span>
    </div>
  </section>
</body>
</html>
```